Poster for Office

Looking for an edgy, beautiful poster to hang up in my office that uses the quotes located below and potentially the image attached.
Content for poster

Title: Pell's Rules

Must have the following quotes included (punctuation and capitalization are flexible, do what you think looks the best they also don't need the quotation symbols):

"Don't order fish at a steakhouse"
"Be bold. The more you tell, the more you sell"
"admit nothing, deny everything, launch counterattack."
"avoid obviousness"
"never do anything until you're ready to do it"
"look good=feel good"
"always keep the advantage"
"never complain, never explain"
"Lay low, play dumb, keep moving"

Industry/Entity Type

Quotes

Requirements
Must have
• Title: Pell's Rules

"avoid obviousness"
"look good=feel good"

```html
<!DOCTYPE html>
<html lang="en">
<head>
<meta charset="utf-8">
<title>Pell's Rules</title>
<link rel="stylesheet" href="https://fonts.googleapis.com/css2?family=Bebas+Neue&family=Amaranth:wght@700&display=swap">
<style>
  :root {
    --sky-deep: #1f63c9;
    --sky-mid: #3fb4e0;
    --sky-pale: #bfe6ea;
    --haze: #f3ecc8;
    --land-warm: #d8a28a;
    --land-red: #c5546a;
    --road-violet: #7a4e9a;
    --road-deep: #2a2f86;
    --title-fill: #e8f7fb;
    --title-edge: #2a8cb3;
    --rule-text: #fbf6dc;
    --rule-shadow: rgba(10, 10, 20, 0.95);
  }
  html, body {
    margin: 0;
    padding: 0;
    overflow: hidden;
    background: #ffffff;
  }
  .poster {
    position: relative;
    width: 855px;
    height: 1200px;
    overflow: hidden;
  }
  .backdrop {
    position: absolute;
    inset: 0;
    background:
      radial-gradient(ellipse 45% 22% at 50% 0%, rgba(255,255,255,0.55), rgba(255,255,255,0) 70%),
      linear-gradient(180deg,
        var(--sky-deep) 0%,
        var(--sky-mid) 18%,
        var(--sky-pale) 38%,
        var(--haze) 58%,
        var(--land-warm) 72%,
        var(--land-red) 80%,
        var(--road-violet) 88%,
        var(--road-deep) 100%);
  }
  .title {
    position: absolute;
    top: 52px;
    left: 0;
    width: 100%;
    margin: 0;
    text-align: center;
    font-family: "Bebas Neue", "Arial Narrow", sans-serif;
    font-weight: 400;
    font-size: 118px;
    line-height: 0.82;
    letter-spacing: 1px;
    color: var(--title-fill);
    text-shadow:
      0 0 2px var(--title-edge),
      2px 3px 0 var(--title-edge),
      3px 5px 6px rgba(20, 60, 110, 0.6);
  }
  .rules {
    position: absolute;
    top: 372px;
    left: 0;
    width: 100%;
    margin: 0;
    padding: 0;
    list-style: none;
    text-align: center;
    font-family: "Amaranth", "Trebuchet MS", sans-serif;
    font-weight: 700;
    font-size: 26px;
    line-height: 1;
    color: var(--rule-text);
  }
  .rules li {
    height: 74.6px;
    text-shadow:
      0 0 3px var(--rule-shadow),
      0 0 6px var(--rule-shadow),
      1px 1px 2px var(--rule-shadow);
  }
</style>
</head>
<body>
  <main class="poster">
    <div class="backdrop" role="img" aria-label="Photograph of a bright blue sky with clouds above a straight open road running through red desert hills"></div>
    <h1 class="title">Pells<br>Rules</h1>
    <ul class="rules">
      <li>Don't order fish at a steakhouse.</li>
      <li>Be bold. The more you tell, the more you sell.</li>
      <li>Admit nothing, deny everything, launch counterattack.</li>
      <li>Avoid obviousness.</li>
      <li>Never do anything until you're ready to do it.</li>
      <li>Look good, feel good.</li>
      <li>Always keep the advantage.</li>
      <li>Never complain, never explain.</li>
      <li>Lay low, play dumb, keep moving.</li>
    </ul>
  </main>
</body>
</html>
```